CD Cover Design Project For New Electronic Album

Hi, I need cover artwork for my forth coming electronic music album. The requirement is for the single page front insert and also the tray liner (rear inlay). You can find the required specifications here http://www.brightpressing.example.co.uk/artwork_specs.php

The title of the album is Lumentide and the artists name is Owen Tasker.

The theme of the album is the world and water, so that needs to play a big part in the imagery. An example of the kind of thing I'm looking for can be found at

http://www.vistaplates.example.com/media/482730/view (this image is copyrighted, so please don't use for your own work).

I have no preference for the rear inlay, so please feel free to come up with something, so long as it is in keeping with the design for the front. There needs to be room for the song titles though, but not sure how many yet!

Good luck!
Updates

If you would like to hear a small section of the type of music to be on the album, you can listen at my tunevault account.

https://tunevault.example.com/quiet-lattice/sets/lumentide

This also contains a mock up of an album cover that was originally thought of, however permission could not be gained for the use of the image.

Industry/Entity Type

Electronic

```html
<!DOCTYPE html>
<html lang="en">
<head>
<meta charset="utf-8">
<title>Lumentide — Owen Tasker</title>
<link rel="stylesheet" href="https://fonts.googleapis.com/css2?family=Quicksand:wght@300;400&display=swap">
<style>
  :root {
    --space-deep: #140b17;
    --space-mid: #2a1733;
    --space-haze: #4a2f5e;
    --ocean-deep: #1d2f6b;
    --ocean-light: #3f62a8;
    --cloud: #e7ecf3;
    --land: #b5a27c;
    --title: #ffffff;
    --artist: #ddd3ea;
  }
  html, body {
    margin: 0;
    padding: 0;
    overflow: hidden;
    background: var(--space-deep);
  }
  .cover {
    position: relative;
    width: 1200px;
    height: 1191px;
    overflow: hidden;
    background:
      radial-gradient(ellipse 60% 40% at 15% 10%, var(--space-haze) 0%, transparent 70%),
      radial-gradient(ellipse 55% 35% at 70% 95%, var(--space-haze) 0%, transparent 70%),
      radial-gradient(ellipse 80% 80% at 50% 45%, var(--space-mid) 0%, var(--space-deep) 80%);
    font-family: "Quicksand", sans-serif;
  }
  .cover__globe {
    position: absolute;
    left: 228px;
    top: 170px;
    width: 744px;
    height: 744px;
  }
  .cover__title {
    position: absolute;
    left: 102px;
    top: 915px;
    margin: 0;
    font-weight: 300;
    font-size: 162px;
    line-height: 1;
    letter-spacing: 2px;
    color: var(--title);
  }
  .cover__artist {
    position: absolute;
    right: 117px;
    top: 1087px;
    margin: 0;
    font-weight: 300;
    font-size: 46px;
    line-height: 1;
    letter-spacing: 1px;
    color: var(--artist);
  }
</style>
</head>
<body>
  <main class="cover">
    <svg class="cover__globe" viewBox="0 0 744 744" role="img" aria-label="Photograph of planet Earth seen from space, showing North America under swirling clouds, with a large water droplet resting on the continent">
      <defs>
        <radialGradient id="globe-fill" cx="45%" cy="38%" r="65%">
          <stop offset="0%" stop-color="var(--land)"/>
          <stop offset="28%" stop-color="var(--ocean-light)"/>
          <stop offset="65%" stop-color="var(--ocean-deep)"/>
          <stop offset="100%" stop-color="#0d1533"/>
        </radialGradient>
        <radialGradient id="globe-cloud" cx="40%" cy="70%" r="60%">
          <stop offset="0%" stop-color="var(--cloud)" stop-opacity="0.45"/>
          <stop offset="100%" stop-color="var(--cloud)" stop-opacity="0"/>
        </radialGradient>
        <radialGradient id="globe-drop" cx="45%" cy="40%" r="60%">
          <stop offset="0%" stop-color="#f4f2f6" stop-opacity="0.8"/>
          <stop offset="100%" stop-color="#c9c6d0" stop-opacity="0.35"/>
        </radialGradient>
      </defs>
      <circle cx="372" cy="372" r="370" fill="url(#globe-fill)"/>
      <circle cx="372" cy="372" r="370" fill="url(#globe-cloud)"/>
      <circle cx="345" cy="265" r="105" fill="url(#globe-drop)"/>
    </svg>

    <h1 class="cover__title">Lumentide</h1>
    <p class="cover__artist">Owen Tasker</p>
  </main>
</body>
</html>
```